Software Business needs a 2 or 4 page brochure design

We develop Microsoft Word Business Proposal Software. This brochure or datasheet will describe our product offering. Depending on the finished design this may be a 4 page bi-fold or a single page datasheet, whichever the designer feels is more compelling.

We need the design completed with Adobe InDesign and Photoshop with the finished work returned as editable in InDesgn.

Microsoft Word draft and Graphics files are attached for review.

Cover designs are impressive however a key element in our market is that many, if not most, of the decision makers are women. So covers showing only businessmen stock photos are probably not sensitive to the reality of the market space we are in.

Reason: End deadline on a weekday.

Please check companion project for one page advert to go with Brochure. Note that this deadline is shorter as the ad needs to be submitted by Monday AM latest: August 18. "Software Company 1pg Print Advertisement"

Industry/Entity Type

Business

```html
<!DOCTYPE html>
<html lang="en">
<head>
<meta charset="utf-8">
<title>Quorventix Software – Automated RFP Response and Document Creation Software</title>
<link rel="stylesheet" href="https://fonts.googleapis.com/css2?family=Oswald:wght@300;500&family=Open+Sans:wght@700&display=swap">
<style>
  :root {
    --page: #ffffff;
    --violet-deep: #4a3a8f;
    --violet-mid: #7a45a6;
    --magenta: #c24e9f;
    --pink-soft: #d56aae;
    --ink-light: #ffffff;
  }
  html, body {
    margin: 0;
    padding: 0;
    width: 848px;
    height: 1200px;
    overflow: hidden;
    background: var(--page);
  }
  .cover {
    position: relative;
    width: 848px;
    height: 1200px;
  }
  .cover-art {
    position: absolute;
    left: 0;
    top: 0;
    width: 848px;
    height: 1200px;
  }
  .headline {
    font-family: "Oswald", "Arial Narrow", sans-serif;
    font-weight: 300;
    fill: var(--ink-light);
  }
  .brand-name {
    font-family: "Oswald", "Arial Narrow", sans-serif;
    font-weight: 500;
    fill: var(--ink-light);
  }
  .brand-tagline {
    font-family: "Open Sans", Arial, sans-serif;
    font-weight: 700;
    fill: var(--ink-light);
  }
  .frame-line {
    fill: none;
    stroke: var(--ink-light);
    stroke-width: 4;
  }
  .frame-line--bold {
    stroke-width: 6;
  }
</style>
</head>
<body>
<main class="cover">
  <svg class="cover-art" viewBox="0 0 848 1200" xmlns="http://www.w3.org/2000/svg">
    <defs>
      <linearGradient id="coverGradient" x1="0" y1="0" x2="0.25" y2="1">
        <stop offset="0" stop-color="var(--violet-deep)"/>
        <stop offset="0.38" stop-color="#5a3d98"/>
        <stop offset="0.62" stop-color="var(--violet-mid)"/>
        <stop offset="0.85" stop-color="var(--pink-soft)"/>
        <stop offset="1" stop-color="var(--magenta)"/>
      </linearGradient>
      <clipPath id="cardClip">
        <rect x="47" y="14" width="754" height="1169" rx="44"/>
      </clipPath>
    </defs>

    <rect class="cover-background" x="47" y="14" width="754" height="1169" rx="44"
          fill="url(#coverGradient)" role="img"
          aria-label="Faceted geometric pattern of overlapping translucent triangles in violet and pink"/>

    <g class="brand">
      <text class="brand-name" x="271" y="198" font-size="50" textLength="307" lengthAdjust="spacingAndGlyphs">QUORVENTIX</text>
      <text class="brand-name" x="307" y="229" font-size="28" textLength="264" lengthAdjust="spacing">Software</text>
      <text class="brand-tagline" x="268" y="254" font-size="15" textLength="300" lengthAdjust="spacingAndGlyphs">The Craft of Proposal Assembly</text>
    </g>

    <g class="frame-lines" clip-path="url(#cardClip)">
      <path class="frame-line" d="M354,493 H737 V714 H718"/>
      <path class="frame-line" d="M585,550 H773 V871 H801"/>
      <path class="frame-line frame-line--bold" d="M148,528 V1183"/>
      <path class="frame-line" d="M207,603 V1183"/>
      <path class="frame-line" d="M291,668 V778 H554 V1183"/>
      <path class="frame-line" d="M698,752 V1183"/>
    </g>

    <g class="headline-block">
      <text class="headline" x="137" y="511" font-size="47" textLength="211" lengthAdjust="spacingAndGlyphs">AUTOMATED</text>
      <text class="headline" x="196" y="590" font-size="92" textLength="374" lengthAdjust="spacingAndGlyphs">RFP RESPONSE</text>
      <text class="headline" x="268" y="650" font-size="30" textLength="40" lengthAdjust="spacingAndGlyphs">AND</text>
      <text class="headline" x="315" y="650" font-size="47" textLength="360" lengthAdjust="spacingAndGlyphs">DOCUMENT CREATION</text>
      <text class="headline" x="428" y="733" font-size="88" textLength="282" lengthAdjust="spacingAndGlyphs">SOFTWARE</text>
    </g>
  </svg>
</main>
</body>
</html>
```